WordPress Design for both website and landing page for an expert

I need a clean and stylish design for my new website. I work as an expert (see attached file WHY HOW WHAT), my product is expert opinion (reports) for company evaluations You can use all of the attached pictures colored or black / white. The person is me, you can add other pictures, if you want. The design should be clean and stylish, so you could use white, black, gray, silver and / or one additional color. I have added an idea about my website, see attached file CONCEPT WEBSITE If you have any more information, please do not hesitate to contact us 'Hesitate to ask me ...

```html
<!DOCTYPE html>
<html lang="de">
<head>
<meta charset="utf-8">
<title>Lukas Verholt – Sachverständiger für Firmenbewertungen</title>
<link rel="stylesheet" href="https://fonts.googleapis.com/css2?family=Montserrat:wght@400;500;600;700&family=Open+Sans:wght@400;600;700&display=swap">
<style>
  :root{
    --teal:#21a9c3;
    --teal-dark:#1a93ab;
    --ink:#1f2224;
    --text:#4a4f53;
    --muted:#6d7377;
    --label:#474d52;
    --line:#b9bdc0;
    --soft:#eef0f1;
    --footer:#1c1d1f;
    --footer-text:#d8d8d8;
    --white:#ffffff;
  }
  *{box-sizing:border-box;margin:0;padding:0}
  html,body{width:1200px;height:2961px;overflow:hidden}
  body{position:relative;background:var(--white);font-family:"Open Sans",Arial,sans-serif;color:var(--text)}
  .abs{position:absolute}

  /* header */
  .site-header{position:absolute;left:0;top:0;width:1200px;height:125px;background:var(--white)}
  .brand{position:absolute;left:110px;top:44px;display:flex;align-items:center;gap:12px;font-family:"Montserrat",sans-serif;font-size:20px;font-weight:500;letter-spacing:2px;color:#7d8387}
  .brand-mark{width:26px;height:26px;border:2px solid #7d8387}
  .main-nav{position:absolute;top:52px;left:436px;display:flex;gap:23px;font-family:"Montserrat",sans-serif;font-size:15px;font-weight:500;color:var(--ink);letter-spacing:.3px}
  .nav-search{position:absolute;left:1070px;top:53px}

  /* hero */
  .hero{position:absolute;left:0;top:125px;width:1200px;height:558px;
    background:linear-gradient(90deg,#e4e4e2 0%,#dcdbd8 45%,#c9c5c0 62%,#d8d5d1 80%,#bfb3a6 100%)}
  .hero-photo{position:absolute;left:560px;top:0;width:640px;height:558px;
    background:radial-gradient(ellipse at 55% 40%,rgba(244,244,244,.9) 0%,rgba(220,216,212,.6) 40%,rgba(200,160,130,.25) 75%,transparent 100%)}
  .hero h1{position:absolute;left:110px;top:265px;font-family:"Montserrat",sans-serif;font-weight:500;font-size:40px;line-height:54px;color:var(--ink)}
  .hero .lead{position:absolute;left:112px;top:393px;font-family:"Montserrat",sans-serif;font-weight:500;font-size:20px;line-height:31px;color:#3e4346;letter-spacing:.3px}
  .btn{display:flex;align-items:center;justify-content:center;font-family:"Montserrat",sans-serif;font-weight:700;text-transform:uppercase}
  .btn-teal{background:var(--teal);color:var(--white)}
  .hero .btn{position:absolute;left:112px;top:478px;width:175px;height:50px;font-size:17px;gap:6px}

  /* reasons */
  .reasons-mark{position:absolute;left:572px;top:760px;width:56px;height:56px;border:3px solid #8a9094}
  .section-title{position:absolute;left:0;width:1200px;text-align:center;font-family:"Montserrat",sans-serif;color:var(--ink)}
  .reasons-title{top:830px;font-size:34px;font-weight:700}
  .reasons-sub{top:880px;font-size:20px;font-weight:500;letter-spacing:.5px}
  .timeline-line{position:absolute;left:599px;top:1025px;width:2px;height:523px;background:var(--line)}
  .icon-box{position:absolute;left:566px;width:68px;height:68px;background:var(--white);border:2px solid #5d6367;display:flex;align-items:center;justify-content:center}
  .reason-label{position:absolute;height:42px;background:var(--label);color:var(--white);font-family:"Montserrat",sans-serif;font-size:22px;font-weight:500;letter-spacing:2px;display:flex;align-items:center;justify-content:center}
  .reason-text{position:absolute;width:330px;font-size:14px;line-height:26px;color:var(--muted)}
  .reason-text.left{text-align:right}

  /* motives */
  .motives{position:absolute;left:0;top:1548px;width:1200px;height:672px;
    background:linear-gradient(180deg,#f1f2f3 0%,#e9ebec 55%,#f3f4f5 100%)}
  .motives-tab{position:absolute;left:555px;top:1548px;width:90px;height:62px;background:var(--white);display:flex;align-items:center;justify-content:center}
  .motives-tab span{width:30px;height:30px;border:3px solid #8a9094}
  .photo-frame{position:absolute;border:5px solid var(--white);box-shadow:0 2px 8px rgba(0,0,0,.18)}
  .photo-office{left:112px;top:1683px;width:314px;height:295px;background:linear-gradient(135deg,#9fb1bf 0%,#6d7d88 45%,#c3ccd2 100%)}
  .photo-portrait{left:252px;top:1877px;width:294px;height:236px;background:linear-gradient(90deg,#cfd3d4 0%,#8c8f8f 35%,#3c3f42 55%,#a9adae 75%,#e1e3e3 100%)}
  .motives h2{position:absolute;left:598px;top:1672px;font-family:"Montserrat",sans-serif;font-size:34px;line-height:46px;font-weight:500;color:var(--ink)}
  .motive-list{position:absolute;left:598px;top:1795px;width:490px;list-style:none}
  .motive-list li{position:relative;padding-left:34px;font-size:13px;line-height:21px;color:var(--text);margin-bottom:20px;text-align:justify}
  .motive-list li::before{content:"";position:absolute;left:1px;top:4px;width:11px;height:11px;border-radius:50%;background:var(--teal);box-shadow:inset 0 0 0 3px var(--teal),inset 0 0 0 4px #fff}
  .motive-note{position:absolute;left:598px;width:490px;font-size:13px;line-height:21px;color:var(--text);text-align:justify}

  /* promise */
  .promise-title{position:absolute;left:110px;font-family:"Montserrat",sans-serif;font-size:19px;font-weight:500;color:var(--ink)}
  .promise-text{position:absolute;left:110px;width:640px;font-size:12px;line-height:24px;color:var(--text)}
  .promise-btn{position:absolute;font-size:16px;height:48px}
  .btn-outline{background:var(--white);color:var(--teal);border:1px solid #cfd3d6}

  /* footer */
  .site-footer{position:absolute;left:0;top:2600px;width:1200px;height:361px;background:var(--footer);color:var(--footer-text)}
  .footer-head{position:absolute;font-family:"Montserrat",sans-serif;font-size:16px;font-weight:700;color:var(--white)}
  .contact-row{position:absolute;left:112px;display:flex;align-items:center;gap:16px;font-size:13px;color:var(--footer-text)}
  .newsletter-input{position:absolute;left:455px;top:2718px;width:297px;height:40px;border:1px solid #d0d0d0;display:flex;align-items:center;justify-content:space-between;padding:0 12px;font-size:14px;color:#e0e0e0}
  .newsletter-btn{position:absolute;left:455px;top:2773px;width:123px;height:37px;font-size:13px}
  .social{position:absolute;top:2720px;left:915px;display:flex;gap:8px}
  .social span{width:36px;height:36px;border-radius:50%;border:2px solid #7b8084}
  .footer-rule{position:absolute;left:112px;top:2860px;width:976px;height:1px;background:#5a5d60}
  .copyright{position:absolute;left:0;top:2900px;width:1200px;text-align:center;font-size:15px;color:var(--white)}
  .copyright .sep{margin:0 16px}
</style>
</head>
<body>

<header class="site-header">
  <div class="brand"><span class="brand-mark"></span>LUKAS VERHOLT</div>
  <nav class="main-nav">
    <span>HOME</span><span>WHAT I DO</span><span>WHY I DO IT &amp; HOW I DO IT</span><span>ABOUT ME</span><span>CONTACT</span>
  </nav>
  <svg class="nav-search" width="16" height="16" viewBox="0 0 16 16"><circle cx="6.5" cy="6.5" r="5" fill="none" stroke="#1f2224" stroke-width="2.2"/><line x1="10.2" y1="10.2" x2="15" y2="15" stroke="#1f2224" stroke-width="2.6"/></svg>
</header>

<section class="hero">
  <div class="hero-photo" role="img" aria-label="Portrait of the expert in a white shirt leaning on a railing, looking into the distance"></div>
</section>
<h1 class="hero abs" style="position:absolute;left:110px;top:265px;width:auto;height:auto;background:none;font-family:'Montserrat',sans-serif;font-weight:500;font-size:40px;line-height:54px;color:var(--ink)">Sachverständiger<br>Für Firmenbewertungen</h1>
<p class="abs" style="left:112px;top:393px;font-family:'Montserrat',sans-serif;font-weight:500;font-size:20px;line-height:31px;color:#3e4346;letter-spacing:.3px">Sie benötigen ein Gutachten zur Ermittlung des<br>Wertes Ihres Unternehmens</p>
<a class="btn btn-teal abs" style="left:112px;top:478px;width:175px;height:50px;font-size:17px;gap:6px">Read More
  <svg width="17" height="17" viewBox="0 0 17 17"><circle cx="8.5" cy="8.5" r="8.5" fill="#fff"/><path d="M6 4.5l4 4-4 4" fill="none" stroke="#21a9c3" stroke-width="2.4"/></svg>
</a>

<section class="reasons">
  <div class="reasons-mark"></div>
  <h2 class="section-title reasons-title">3 REASONS</h2>
  <p class="section-title reasons-sub">WHY YOU SHOULD WORK WITH ME</p>

  <div class="timeline-line"></div>

  <div class="reason-label" style="left:330px;top:968px;width:190px">SCHNELL</div>
  <div class="icon-box" style="top:957px">
    <svg width="44" height="44" viewBox="0 0 44 44" fill="none" stroke="#21a9c3" stroke-width="2"><circle cx="22" cy="25" r="14"/><line x1="22" y1="6" x2="22" y2="11"/><line x1="18" y1="5" x2="26" y2="5"/><path d="M22 25V16M22 25l6 4"/><line x1="4" y1="20" x2="10" y2="20" stroke="#4a4f53"/><line x1="2" y1="26" x2="8" y2="26" stroke="#4a4f53"/></svg>
  </div>
  <p class="reason-text" style="left:680px;top:962px">Sie bekommen Ihr Gutachten zeitnah (innerhalb von max. 21 Tagen nach Zugang aller benötigten Unterlagen)</p>

  <p class="reason-text left" style="left:190px;top:1152px">Sie erhalten ein qualifiziertes und belastbares Gutachten von einem zertifizierten Sachverständigen (höchste Akzeptanz bei allen Parteien)</p>
  <div class="icon-box" style="top:1148px">
    <svg width="44" height="44" viewBox="0 0 44 44" fill="none" stroke="#21a9c3" stroke-width="2"><rect x="6" y="18" width="20" height="20" stroke="#4a4f53"/><path d="M10 28l4 4 8-9"/><rect x="28" y="26" width="10" height="12" stroke="#4a4f53"/><path d="M10 8l1.5 3 3 .4-2.2 2 .6 3-2.9-1.5L7.1 16.4l.6-3-2.2-2 3-.4z"/><path d="M22 4l1.5 3 3 .4-2.2 2 .6 3-2.9-1.5-2.9 1.5.6-3-2.2-2 3-.4z"/><path d="M34 8l1.5 3 3 .4-2.2 2 .6 3-2.9-1.5-2.9 1.5.6-3-2.2-2 3-.4z"/></svg>
  </div>
  <div class="reason-label" style="left:680px;top:1160px;width:212px">ZERTIFIZIERT</div>

  <div class="reason-label" style="left:293px;top:1355px;width:227px">VERSTÄNDLICH</div>
  <div class="icon-box" style="top:1345px">
    <svg width="44" height="44" viewBox="0 0 44 44" fill="none" stroke="#21a9c3" stroke-width="2"><path d="M22 8a9 9 0 0 0-5 16.5V29h10v-4.5A9 9 0 0 0 22 8z"/><line x1="18" y1="33" x2="26" y2="33" stroke="#4a4f53"/><line x1="19" y1="37" x2="25" y2="37" stroke="#4a4f53"/><path d="M22 2v3M9 7l2 2M35 7l-2 2M4 17h3M37 17h3" stroke="#4a4f53"/></svg>
  </div>
  <p class="reason-text" style="left:680px;top:1350px">Sie bekommen Ihr Gutachten zeitnah (innerhalb von max. 21 Tagen nach Zugang aller benötigten Unterlagen)</p>
</section>

<section class="motives">
  <div class="motives-tab"><span></span></div>
</section>
<div class="motives-tab"><span></span></div>
<div class="photo-frame photo-office" role="img" aria-label="Business analysis charts and a hand with a pen at a desk"></div>
<div class="photo-frame photo-portrait" role="img" aria-label="The expert in a dark suit standing in a bright office corridor"></div>
<h2 class="abs" style="left:598px;top:1672px;font-family:'Montserrat',sans-serif;font-size:34px;line-height:46px;font-weight:500;color:var(--ink)">WAS SIND DIE KAUFMOTIVE<br>DER KUNDEN?</h2>
<ul class="motive-list">
  <li>Sie wollen Anteile Ihres Unternehmens oder ihr gesamtes Unternehmen verkaufen?</li>
  <li>Sie wollen Ihr Unternehmen auf Ihre Erben übertragen und benötigen eine Bewertung für das Finanzamt?</li>
  <li>Sie müssen im Rahmen einer Trennung/Scheidung jemanden ausbezahlen und benötigen eine Bemessungsgrundlage?</li>
</ul>
<p class="motive-note" style="top:1992px">Lassen Sie Ihr Unternehmen von einem qualifizierten Sachverständigen bewerten und gehen somit vielen (unnötigen) Streitereien aus dem Weg.</p>
<p class="motive-note" style="top:2052px">Merke: Die Kosten für ein Gutachten sind immer überproportional günstiger als die Kosten für Rechtsstreitigkeiten. Und das losgelöst von der psychischen Belastung einer solchen Auseinandersetzung ...</p>

<section class="promise">
  <h3 class="promise-title" style="top:2318px">My Quality Promise:</h3>
  <p class="promise-text" style="top:2356px">should the advised date for the preparation of the report be exceeded, you will receive the report free of chare.</p>
  <a class="btn btn-teal promise-btn" style="left:905px;top:2322px;width:183px">I Waive My Fee</a>

  <h3 class="promise-title" style="top:2432px">Mein Qualitätsversprechen:</h3>
  <p class="promise-text" style="top:2470px">Sollte der avisierte Termin für die Erstellung des Gutachtens überschritten werden, erhalten Sie das Gutachten absolut kostenfrei!</p>
  <a class="btn btn-outline promise-btn" style="left:763px;top:2437px;width:325px">Ich verzichte auf mein Honorar</a>
</section>

<footer class="site-footer"></footer>
<h4 class="footer-head" style="left:112px;top:2678px">CONTACT US</h4>
<div class="contact-row" style="top:2730px">
  <svg width="14" height="14" viewBox="0 0 14 14"><path d="M3 1l2.5 3-1.3 1.6a8 8 0 0 0 4.2 4.2L10 8.5l3 2.5-1.5 2.2C6 13 1 8 .8 2.5z" fill="#fff"/></svg>
  (+1) 555 010 2040
</div>
<div class="contact-row" style="top:2774px">
  <svg width="14" height="11" viewBox="0 0 14 11"><rect width="14" height="11" fill="#fff"/><path d="M0 0l7 6 7-6" fill="none" stroke="#1c1d1f" stroke-width="1.4"/></svg>
  support@lukasverholt.com
</div>

<h4 class="footer-head" style="left:453px;top:2678px">NEWSLETTER SUBSCRIBE</h4>
<div class="newsletter-input">Enter Email
  <svg width="14" height="11" viewBox="0 0 14 11"><rect width="14" height="11" fill="#fff"/><path d="M0 0l7 6 7-6" fill="none" stroke="#1c1d1f" stroke-width="1.4"/></svg>
</div>
<a class="btn btn-teal newsletter-btn">Subscribe</a>

<h4 class="footer-head" style="left:915px;top:2678px">FOLLOW US ON</h4>
<div class="social"><span></span><span></span><span></span><span></span></div>

<div class="footer-rule"></div>
<p class="copyright">Copyrights © 2018 Lukas Verholt. All Rights Reserved<span class="sep">|</span>Privacy Policy<span class="sep">|</span>Terms Of Services.</p>

</body>
</html>
```